Real estate company needs a letterhead design

A young real estate company needs a letterhead / stationery design, it should include the company's logo. It should look exactly the same as on the business cards. (With the phrase "a brand of FEO Immobilien & Projektentwicklung GmbH")

In addition, it should also include the 4 round seals.

color code blue # 00456b gray # 333333

Word and PDF are welcome.

FEO Immobilien & Projektentwicklung GmbH
Managing director: Mag. Lukas Strenhofer
Anton-Wiesmayr-Strasse 3c / 41
6300 Wörgl

Tel .: +436645917283
Email: office@wohnquell.example
Web: www.wohnquell.example

Sparkasse Almhofen, Bergländer Sparkasse from 1893, Gildenkasse
Ferdinand-Moosrainer-Strasse 9, 6300 Wörgl
IBAN: AT31 4819 2093 5521 6604
BIC: GLMRAT31XXX
Account holder: FEO Immobilien & Projektentwicklung GmbH

FN: XXXXXXX
UID: XXXXXXX

```html
<!DOCTYPE html>
<html lang="de">
<head>
<meta charset="utf-8">
<title>Letterhead – WOHNQUELL</title>
<link rel="stylesheet" href="https://fonts.googleapis.com/css2?family=Montserrat:wght@300;400&family=Arimo:wght@400;700&display=swap">
<style>
  :root {
    --brand-blue: #00456b;
    --brand-gray: #333333;
    --text-light: #8a8a8a;
    --seal-tone: #e9c9c6;
    --backdrop: #dfe6ec;
    --paper: #ffffff;
  }
  * { box-sizing: border-box; margin: 0; padding: 0; }
  html, body { width: 1200px; height: 1200px; overflow: hidden; background: var(--backdrop); }
  .sheet {
    position: absolute; left: 176px; top: 0; width: 848px; height: 1200px;
    background: var(--paper); font-family: "Montserrat", sans-serif; color: var(--brand-gray);
  }
  .header-rule-blue { position: absolute; left: 0; right: 0; top: 132px; height: 7px; background: var(--brand-blue); }
  .header-rule-gray { position: absolute; left: 0; right: 0; top: 145px; height: 3px; background: var(--brand-gray); }
  .brand { position: absolute; left: 48px; top: 82px; }
  .brand-name { font-weight: 400; font-size: 36px; color: var(--brand-blue); line-height: 44px; }
  .brand-tagline {
    position: absolute; left: 46px; top: 130px; padding: 0 4px; background: var(--paper);
    font-family: "Arimo", sans-serif; font-size: 9.5px; color: var(--brand-blue); line-height: 12px;
  }
  .seals { position: absolute; left: 516px; top: 38px; width: 90px; height: 90px; }
  .bank { position: absolute; left: 617px; top: 36px; font-family: "Arimo", sans-serif; font-size: 14px; line-height: 17px; color: #222; font-style: normal; }
  .recipient { position: absolute; left: 85px; top: 268px; }
  .recipient .label { font-size: 14px; letter-spacing: 2px; color: var(--brand-gray); }
  .recipient .name { font-size: 14px; color: var(--brand-blue); margin-top: 8px; }
  .recipient .lines { font-weight: 300; font-size: 11px; line-height: 19px; color: var(--text-light); margin-top: 6px; }
  .date { position: absolute; right: 87px; top: 268px; font-size: 11.5px; color: var(--brand-gray); }
  .body-copy { position: absolute; left: 85px; top: 430px; width: 676px; font-weight: 300; font-size: 11.5px; line-height: 15px; color: var(--text-light); text-align: justify; }
  .body-copy p { margin-bottom: 15px; }
  .signature-mark { position: absolute; left: 84px; top: 846px; width: 150px; height: 36px; }
  .signer { position: absolute; left: 83px; top: 892px; }
  .signer .name { font-size: 13px; color: var(--brand-gray); }
  .signer .role { font-weight: 300; font-size: 10.5px; color: var(--text-light); margin-top: 2px; }
  .footer { position: absolute; left: 55px; top: 1103px; display: flex; font-family: "Arimo", sans-serif; font-size: 13px; line-height: 16.5px; color: #222; }
  .footer b { color: var(--brand-blue); }
  .footer-col { padding-right: 20px; }
  .footer-col + .footer-col { border-left: 1.5px solid var(--brand-gray); padding-left: 20px; }
</style>
</head>
<body>
<main class="sheet">
  <div class="header-rule-blue"></div>
  <div class="header-rule-gray"></div>
  <div class="brand"><span class="brand-name">WOHNQUELL</span></div>
  <div class="brand-tagline">eine Marke der FEO Immobilien &amp; Projektentwicklung GmbH</div>

  <svg class="seals" viewBox="0 0 90 90" role="img" aria-label="Four round bank seals">
    <g fill="var(--seal-tone)">
      <circle cx="21" cy="21" r="20"/><circle cx="66" cy="21" r="20"/>
      <circle cx="21" cy="66" r="20"/><circle cx="66" cy="66" r="20"/>
    </g>
  </svg>

  <address class="bank">
    Sparkasse Almhofen<br>
    Bergländer Sparkasse from 1893<br>
    Gildenkasse<br>
    Ferdinand-Moosrainer-Strasse 9<br>
    6300 Wörgl
  </address>

  <section class="recipient">
    <div class="label">TO</div>
    <div class="name">Petra Lindqvist</div>
    <div class="lines">Human Resources<br>Norvale Inc.<br>2207-B Harlow Lane, Fenbrook<br>F41 USA</div>
  </section>
  <div class="date">Friday, 01/01/2018</div>

  <section class="body-copy">
    <p>Lorem ipsum dolor sit amet, consectetuer adipiscing elit, sed diam nonmmy nibh euismod tincidunt ut laoreet dolore magna aliquam erat volutpat. Ut wisi enim ad minim veniam, quis nostrud exerci tationmcorper suscipit lobortis nisl ut aliquip ex ea commodo consequat. Duis autem vel eum iriure dolor in hendrerit in vulputate velit esse molestie consequat, vel illum dolore eu feugiat nulla facilisis at vero eros et accumsan et iusto odio dignissim qui blandit praesent luptatum zzril delenit augue duis dolore te feugait nulla facilisi.</p>
    <p>Nam liber tempor cum soluta nobis eleifend option congue nihil imprdiet doming id quod mazim placerat facer possim assum. Typi non habent claritatem insitam;</p>
    <p>Est usus legentis in iis qui facit eorum claritatem.</p>
    <p>Investigationes demonstraverunt lectores legere me lius quod ii legunt saepius. Claritas est etiam processus dynamicus, qui sequitur mutationem consuetudium lectorum. Mirum est notare quam littera gothica, quam nunc putamus parum claram, anteposuerit litterarum formas humanitatis per seacula quarta decima et quinta decima. Eodem modo typi, qui nunc nobis videntur parum clari, fiant sollemnes in futurum.</p>
    <p>consectetuer adipiscing elit, sed diam nonummy nibh euismod tincidunt ut laoreet dolore magna aliquam erat volutpat. Ut wisi enim ad minim veniam, quis nostrud exerci tation ullamcorper suscipit lobortis nisl ut aliquip ex ea commodo consequat. Duis autem vel eum iriure dolor in hendrerit in vulputate velit esse molestie consequat, vel illum dolore eu feugiat nulla facilisis at vero eros et accumsan et iusto odio dignissim qui blandit praesent luptatum zzril delenit augue duis dolore te feugait nulla facilisi.</p>
    <p>Nam liber tempor cum soluta nobis eleifend option congue nihil imperdiet .</p>
  </section>

  <svg class="signature-mark" viewBox="0 0 150 36" role="img" aria-label="Handwritten signature">
    <rect width="150" height="36" rx="4" fill="#ececec"/>
  </svg>
  <div class="signer">
    <div class="name">Henrik Aldous</div>
    <div class="role">Managing Director</div>
  </div>

  <footer class="footer">
    <div class="footer-col">
      <b>Mag. Lukas Strenhofer</b><br>
      Managing director<br>
      Anton-Wiesmayr-Strasse 3c / 41<br>
      6300 Wörgl
    </div>
    <div class="footer-col">
      <b>IBAN:</b> AT31 4819 2093 5521 6604<br>
      <b>BIC:</b> GLMRAT31XXX<br>
      <b>Account holder:</b><br>
      FEO Immobilien &amp; Projektentwicklung GmbH
    </div>
    <div class="footer-col">
      <b>Tel .:</b> +436645917283<br>
      <b>Email:</b> office@wohnquell.example<br>
      <b>Web:</b> www.wohnquell.example<br>
      <b>FN:</b> XXXXXXX | <b>UID:</b> XXXXXXX
    </div>
  </footer>
</main>
</body>
</html>
```